Beauty care products face masks Layout

--- English below --- We need a label set (2 pieces á 35x80mm) for a black 50ml tube. The logo and the subtitles are displayed in the Annexes. A black drop should be incorporated into the label. Brand Name: velaZ Product name: brume subtitles: Deep cleansing peel-off mask required entry is: 50 ml / 1.69 fl.oz. On the back: Recommended use: In order to achieve the best results for you, we recommend that you clean your face thoroughly and dry. Apply the mask, thereby avoiding the mouth and eye area. After 20-30 minutes the mask is dried and can be pulled off. Purify by removing the mask, your face with warm water. We recommend a calming face cream after the application to use. The mask Please do not dispose of in the toilet. Application: Every 2-3 days Ingredients (ingredients): Water, Polyvinyl Alcohol, Glycerin, Citrus Paradisi, PEG-8, panthenol, Fragrance, Cellulose Gum, tetra sodium EDTA, Activated carbon, Rosemary Extract, Avena sativa Extract, Pot Marigold , Zinc Gluconate, lecithin, Retinyl Palmitate, arachidyl propionate, tocopheryl acetate, ethyl Liloenate, xanthan Gum, Limonene, linalool, geraniol, methyl paraben English: We need a label set (2 pieces 35mm wide 80mm height) for a black 50ml tube. You can find the logo as well as the subtitel in the attachments. Brand Name: velaZ Product Name: brume Subtitle: Deep cleansing peel-off mask On the back label: Recommended use: In order to achieve the best results for you, we recommend that you clean your face thoroughly and dry. Apply the mask, thereby avoiding the mouth and eye area. After 20-30 minutes the mask is dried and can be pulled off. Purify by removing the mask, your face with warm water. We recommend a calming face cream after the application to use. The mask Please do not dispose of in the toilet. Application: Every 2-3 days Ingredients (ingredients): Water, Polyvinyl Alcohol, Glycerin, Citrus Paradisi, PEG-8, panthenol, Fragrance, Cellulose Gum, tetra sodium EDTA, Activated carbon, Rosemary Extract, Avena sativa Extract, Pot Marigold , Zinc Gluconate, lecithin, Retinyl Palmitate, arachidyl propionate, tocopheryl acetate, ethyl Liloenate, xanthan Gum, Limonene, linalool, geraniol, methyl paraben

Target Market(s)

Cosmetics, Beauty, Body Care, Women

Requirements
Must have
• Clear lines to possibly expanding the range Clear design for possible other products
Nice to have
• The design should be more female. We prefer a feminine design.

```html
<!DOCTYPE html>
<html lang="de">
<head>
<meta charset="utf-8">
<title>velaZ brume – Etikett</title>
<link rel="stylesheet" href="https://fonts.googleapis.com/css2?family=Encode+Sans+Condensed:wght@400;600&family=Arimo:wght@400&family=Damion&display=swap">
<style>
  :root {
    --page-bg: #d4d4d4;
    --page-bg-edge: #a9a9a9;
    --label-purple: #9a55a6;
    --label-purple-deep: #8a4597;
    --band-lilac: #b87fbe;
    --band-lilac-light: #c796cc;
    --stripe-black: #161616;
    --ink-dark: #2a1a2d;
    --ink-white: #ffffff;
  }
  * { margin: 0; padding: 0; box-sizing: border-box; }
  html, body { width: 1200px; height: 1200px; overflow: hidden; }
  body {
    background: radial-gradient(ellipse at 50% 45%, var(--page-bg) 0%, var(--page-bg) 45%, var(--page-bg-edge) 100%);
    position: relative;
  }
  .label {
    position: absolute;
    left: 350px;
    top: 50px;
    width: 500px;
    height: 1100px;
    background: linear-gradient(160deg, var(--label-purple-deep) 0%, var(--label-purple) 45%, var(--label-purple-deep) 100%);
    overflow: hidden;
    box-shadow: 0 12px 30px rgba(0,0,0,0.18);
  }
  .label__band {
    position: absolute;
    inset: 0;
    width: 500px;
    height: 1100px;
  }
  .brand {
    position: absolute;
    top: 165px;
    left: 0;
    width: 100%;
    text-align: center;
    font-family: "Arimo", sans-serif;
    font-weight: 400;
    font-size: 54px;
    line-height: 1;
    text-transform: uppercase;
    letter-spacing: 10px;
    color: var(--ink-dark);
  }
  .brand__maker {
    position: absolute;
    top: 258px;
    left: 0;
    width: 100%;
    text-align: center;
    font-family: "Arimo", sans-serif;
    font-size: 22px;
    color: var(--ink-dark);
  }
  .product-name {
    position: absolute;
    top: 440px;
    left: 0;
    width: 100%;
    text-align: center;
    font-family: "Encode Sans Condensed", sans-serif;
    font-weight: 400;
    font-size: 160px;
    line-height: 1;
    color: var(--ink-white);
    letter-spacing: -2px;
  }
  .volume {
    position: absolute;
    top: 790px;
    left: 0;
    width: 100%;
    text-align: center;
    font-family: "Encode Sans Condensed", sans-serif;
    font-weight: 600;
    font-size: 30px;
    color: var(--ink-white);
    transform: rotate(-4deg);
  }
  .subtitle {
    position: absolute;
    top: 860px;
    left: 70px;
    width: 380px;
    font-family: "Damion", cursive;
    font-size: 32px;
    line-height: 1.05;
    color: var(--ink-dark);
    transform: rotate(-9deg);
  }
  .subtitle__line { display: block; }
  .subtitle__line--second { padding-left: 95px; }
</style>
</head>
<body>
  <main class="label">
    <svg class="label__band" viewBox="0 0 500 1100" aria-hidden="true">
      <defs>
        <linearGradient id="bandFill" x1="0" y1="0" x2="1" y2="0">
          <stop offset="0" stop-color="#b87fbe"/>
          <stop offset="1" stop-color="#c796cc"/>
        </linearGradient>
      </defs>
      <polygon points="0,370 500,300 500,720 0,775" fill="url(#bandFill)"/>
      <polygon points="0,356 260,318 0,370" fill="#161616"/>
      <polygon points="170,760 500,720 500,730" fill="#161616"/>
    </svg>

    <h1 class="brand">velaZ</h1>
    <p class="brand__maker">Lumora, Lisbon</p>

    <h2 class="product-name">brume</h2>

    <p class="volume">50 ml / 1.69 fl.oz</p>

    <p class="subtitle">
      <span class="subtitle__line">Tiefenreinigende</span>
      <span class="subtitle__line subtitle__line--second">peel-off Maske</span>
    </p>
  </main>
</body>
</html>
```